The Nine Gates for Tablet Reliance - Contemporary Book Cover Design

The Nine Gates for Tablet Reliance was published in March 2019 and is available on Brimora and other platforms now. However, I am not happy with the cover.  It's a good design in some ways - I thought it would stand out and be easily recognizable. But I don't really like the color scheme and feel that a self-help book should probably use some lighter colors and that the red is too strident. The color scheme carries over into other marketing materials like the website, social media, etc. and I don't like the red and black scheme for these purposes.
It's not essential that the cover contain an endorsement like the current one but it could. Here are some endorsements:
“A must-read for anyone who is addicted to or thinks they may have a problem with digital technology. This eloquent work will also be useful to academics and clinicians exploring potential solutions. The author recognizes the similarities between smartphone addiction and other addictions, and logically applies one of the most effective known solutions for addiction - The Nine Gates.”
-- Dale Wickersham: Noted Interventionist, Keynote Speaker and Addiction Visionary
“If you suffer from digital addiction, I strongly encourage you to use this book as your road map to get you back to the real world.”
-- Thomas Quillard, Founder of Online Channel Monitor.
The back cover would have the new design / color scheme, but can have similar text, bio, author image, etc. Or we could include the endorsements there and shorten the other text.
As for the cover it could be stylized, or an image, a partial image, or whatever. I am open to suggestions. Think about what would be inviting for a person searching for help with moderating their smartphone use.
Let's add a subtitle as well "An Inner Journey to Balanced Tablet Habits"
Here is a link to the book:
https://www.brimora.example/Nine-Gates-Tablet-Reliance/dp/4086213590

Target Market(s)
General, since this issue affects almost everyone.
Colors
Designer to choose colors to be used in the design.
Look and feel

```html
<!DOCTYPE html>
<html lang="en">
<head>
<meta charset="utf-8">
<title>The Nine Gates for Tablet Reliance — Cover</title>
<link href="https://fonts.googleapis.com/css2?family=Cinzel:wght@400;700;900&family=Yellowtail&family=Allura&display=swap" rel="stylesheet">
<style>
  :root {
    --paper: #ffffff;
    --ink: #555555;
    --ink-dark: #3f3f3f;
    --gold: #f9b93e;
    --gold-light: #fde3a8;
    --shadow-brown: #5a3b1f;
  }
  html, body {
    margin: 0;
    padding: 0;
    overflow: hidden;
    background: var(--paper);
  }
  .cover {
    position: relative;
    width: 800px;
    height: 1200px;
    background: var(--paper);
    overflow: hidden;
    font-family: "Cinzel", serif;
    color: var(--ink);
  }
  .subtitle {
    position: absolute;
    top: 70px;
    left: 0;
    width: 100%;
    text-align: center;
    font-size: 28px;
    line-height: 40px;
    font-weight: 400;
    margin: 0;
  }
  .title-script {
    position: absolute;
    left: 0;
    width: 100%;
    text-align: center;
    font-family: "Yellowtail", cursive;
    color: var(--gold);
    font-size: 46px;
    line-height: 1;
    margin: 0;
  }
  .title-the { top: 190px; }
  .title-for { top: 318px; }
  .title-main {
    position: absolute;
    top: 252px;
    left: 0;
    width: 100%;
    text-align: center;
    font-size: 52px;
    letter-spacing: 7px;
    font-weight: 400;
    margin: 0;
    line-height: 1;
  }
  .title-big {
    position: absolute;
    left: 0;
    width: 100%;
    text-align: center;
    font-weight: 900;
    color: var(--gold);
    font-size: 84px;
    line-height: 1;
    letter-spacing: 2px;
    text-shadow: 2px 3px 0 var(--shadow-brown);
    margin: 0;
  }
  .title-tablet { top: 390px; }
  .title-reliance { top: 472px; }
  .stair-illustration {
    position: absolute;
    left: 124px;
    top: 625px;
    width: 545px;
    height: 300px;
    background: linear-gradient(160deg, rgba(249,185,62,0) 0%, var(--gold-light) 40%, rgba(249,185,62,0.55) 70%, rgba(249,185,62,0) 100%);
    clip-path: polygon(0 100%, 100% 0, 100% 18%, 8% 100%);
  }
  .endorsement {
    position: absolute;
    right: 153px;
    top: 786px;
    text-align: right;
    font-size: 19px;
    line-height: 24.5px;
    color: var(--ink-dark);
    margin: 0;
  }
  .endorser-name {
    position: absolute;
    right: 153px;
    top: 966px;
    font-family: "Allura", cursive;
    font-size: 34px;
    color: var(--ink-dark);
    margin: 0;
    line-height: 1;
  }
  .endorser-role {
    position: absolute;
    right: 153px;
    top: 1002px;
    font-size: 13.5px;
    color: var(--ink-dark);
    margin: 0;
  }
  .author {
    position: absolute;
    top: 1088px;
    left: 0;
    width: 100%;
    text-align: center;
    font-size: 38px;
    letter-spacing: 6px;
    font-weight: 400;
    margin: 0;
    line-height: 1;
  }
</style>
</head>
<body>
  <main class="cover">
    <p class="subtitle">An Inner Journey to Balanced<br>Tablet Habits</p>

    <h1 class="book-title">
      <span class="title-script title-the">The</span>
      <span class="title-main">NINE GATES</span>
      <span class="title-script title-for">for</span>
      <span class="title-big title-tablet">TABLET</span>
      <span class="title-big title-reliance">RELIANCE</span>
    </h1>

    <div class="stair-illustration" role="img" aria-label="Illustration of a figure leaping up a golden brushstroke staircase"></div>

    <blockquote class="endorsement">“If you<br>suffer from<br>digital addiction,<br>I strongly encourage<br>you to use this book as your<br>road map to get you back to the<br>real world.”</blockquote>
    <p class="endorser-name">Thomas Quillard</p>
    <p class="endorser-role">Founder of Online Channel Monitor</p>

    <p class="author">JONAH VERLADE</p>
  </main>
</body>
</html>
```